Property development company needs a name card design

I started my company since 2010, based in Auckland, New Zealand. We have been doing residential property rentals, individual low-rise residential property construction, small to medium scale residential development project. We will be participate in property investment as well. I have no favor of any specific design or color, just be creative and do anything you think will match the concept.

```html
<!DOCTYPE html>
<html lang="en">
<head>
<meta charset="utf-8">
<title>Kowhai Investment and Development Ltd – Name Card</title>
<link rel="stylesheet" href="https://fonts.googleapis.com/css2?family=Carlito:wght@400;700&display=swap">
<style>
  :root {
    --bg-light: #c2da97;
    --bg-mid: #a9c77f;
    --bg-deep: #8aa663;
    --teal-hint: #8fc0a2;
    --frame-ink: #111111;
    --text-ink: #0d0d0d;
    --band-green: rgba(76, 176, 80, 0.85);
    --band-green-soft: rgba(76, 176, 80, 0.8);
  }
  * { box-sizing: border-box; margin: 0; padding: 0; }
  html, body {
    width: 1200px;
    height: 686px;
    overflow: hidden;
    background: var(--bg-light);
  }
  .card {
    position: relative;
    width: 1200px;
    height: 686px;
    overflow: hidden;
    font-family: "Carlito", "Calibri", sans-serif;
    color: var(--text-ink);
  }
  .card-backdrop {
    position: absolute;
    inset: 0;
    background:
      radial-gradient(circle at 92% 12%, var(--teal-hint) 0%, rgba(143,192,162,0) 22%),
      radial-gradient(circle at 52% 40%, rgba(143,192,162,0.55) 0%, rgba(143,192,162,0) 30%),
      linear-gradient(180deg, var(--bg-light) 0%, var(--bg-mid) 55%, var(--bg-deep) 100%);
  }
  .company-frame {
    position: absolute;
    left: 329px;
    top: 106px;
    width: 617px;
    height: 179px;
    border: 2px solid var(--frame-ink);
    padding: 4px;
  }
  .company-frame-inner {
    width: 100%;
    height: 100%;
    border: 2px solid var(--frame-ink);
    display: flex;
    align-items: center;
    justify-content: center;
  }
  .company-name {
    font-weight: 700;
    font-size: 55px;
    line-height: 1.22;
    text-align: center;
  }
  .band {
    position: absolute;
    left: 57px;
    width: 1086px;
    display: flex;
    align-items: center;
    justify-content: center;
    padding-left: 44px;
    font-weight: 700;
  }
  .band-name {
    top: 466px;
    height: 109px;
    background: var(--band-green);
    font-size: 47px;
  }
  .band-role {
    top: 590px;
    height: 47px;
    background: var(--band-green-soft);
    font-size: 37px;
  }
</style>
</head>
<body>
  <main class="card">
    <div class="card-backdrop" role="img" aria-label="Light green background with teal concentric circles and a darker green city skyline silhouette with a central tower"></div>

    <div class="company-frame">
      <div class="company-frame-inner">
        <h1 class="company-name">Kowhai Investment<br>and Development Ltd</h1>
      </div>
    </div>

    <p class="band band-name">Mei Lin Zhou</p>
    <p class="band band-role">Director</p>
  </main>
</body>
</html>
```